Nine Rung Ledger Remedy Seminar

I would like a flyer to hand out to participants at the speeches that we give. We are a CPA firm that specializes in entrepreneurs and realtors. We would like a flyer that looks crisp and clean, that integrates our logo and our company colors (shades of blue & gold). We would like the wording to be as laid out in the attached documents, but design is up to you. We would like a picture to go along with each point and are open to ideas. The flyer should be one page, preferably just the front.

Colors
3176b5
fee18a

Requirements
Must have
• Our logo and the wording supplied.
• A picture to go along with each topic.
Nice to have
• Images that pop, clean look, professional.
Should not have
• Look messy.

```html
<!DOCTYPE html>
<html lang="en">
<head>
<meta charset="utf-8">
<title>Nine Rung Ledger Remedy Seminar Agenda</title>
<link rel="stylesheet" href="https://fonts.googleapis.com/css2?family=Arimo:wght@400;700&family=Lexend:wght@800&family=Libre+Baskerville:ital@1&family=Comfortaa:wght@300&display=swap">
<style>
:root{
  --page:#e9e9e9;
  --blue:#3176b5;
  --ink:#2c6cad;
  --gold:#fee18a;
  --card-gold:#f3d97f;
  --card-white:#f4f4f4;
  --num:#a9b7cf;
  --white:#ffffff;
}
*{margin:0;padding:0;box-sizing:border-box}
html,body{width:1200px;height:1200px;overflow:hidden;background:var(--page)}
.flyer{position:absolute;left:191px;top:20px;width:818px;height:1160px;background:var(--blue);font-family:"Arimo",Arial,sans-serif;box-shadow:0 6px 18px rgba(0,0,0,.18)}
.brand-badge{position:absolute;left:40px;top:36px;width:232px;height:192px}
.brand-badge svg{position:absolute;inset:0}
.brand-name{position:absolute;left:24px;top:74px;width:170px;text-align:center;font-weight:700;font-size:25px;line-height:1.05;color:var(--ink)}
.tagline{position:absolute;right:55px;top:50px;text-align:right;font-family:"Libre Baskerville",Georgia,serif;font-style:italic;font-size:21px;line-height:29px;color:var(--gold)}
.headline{position:absolute;right:38px;top:196px;width:490px;text-align:right;font-family:"Lexend",Arial,sans-serif;font-weight:800;font-size:30px;line-height:38px;letter-spacing:.3px;color:var(--gold);text-transform:uppercase;white-space:nowrap}
.agenda{position:absolute;left:40px;top:289px;width:738px;display:grid;grid-template-columns:repeat(3,1fr);grid-template-rows:281px 264px;gap:6px}
.step{padding:10px 24px 0 23px;color:var(--ink);font-size:15.5px;line-height:19.8px}
.step--white{background:var(--card-white)}
.step--gold{background:var(--card-gold)}
.step__num{display:block;font-family:"Lexend",Arial,sans-serif;font-weight:800;font-size:16px;color:var(--num);margin-bottom:17px}
.finale{position:absolute;left:40px;top:856px;width:720px;display:flex;color:var(--white);font-size:15.5px;line-height:19.8px}
.finale__num{flex:0 0 57px;padding-left:14px;font-family:"Lexend",Arial,sans-serif;font-weight:800;color:var(--gold)}
.rule{position:absolute;left:40px;top:938px;width:724px;height:2px;background:var(--gold)}
.slogan{position:absolute;left:40px;top:958px;width:380px;font-family:"Comfortaa",sans-serif;font-weight:300;font-size:34px;line-height:39.5px;color:var(--gold)}
.contact{position:absolute;left:467px;top:966px;font-size:14.6px;line-height:18.7px;color:var(--white);font-style:normal}
.contact__name{font-weight:700;color:var(--gold)}
.contact__web{font-weight:700}
.contact__gap{height:18.7px}
</style>
</head>
<body>
<main class="flyer">
  <div class="brand-badge">
    <svg viewBox="0 0 232 192" width="232" height="192" aria-hidden="true">
      <path d="M28 22 C70 -4 170 -4 210 20 C240 40 232 90 200 120 C160 160 90 200 40 180 C0 162 -6 60 28 22 Z" fill="#f1f1f1"/>
    </svg>
    <div class="brand-name">Steady Ledger</div>
  </div>

  <p class="tagline">A professional<br>Accounting Corporation</p>

  <h1 class="headline">Nine Rung Ledger Remedy<br>Seminar Agenda:</h1>

  <section class="agenda">
    <article class="step step--white"><span class="step__num">1</span>We will first show you how to eliminate much of your self-employment tax on your return by converting your business into an S Corporation.&nbsp;&nbsp; A business owner making over $120,000 per year can save about $12,000 per year by doing this.</article>
    <article class="step step--gold"><span class="step__num">2</span>We will show you how to get tax free income from your corporation by renting you home to the corporation for the board meetings. Many of our clients are getting up to $21,000 in tax free income which could put $8,400 cash into your pocket.</article>
    <article class="step step--white"><span class="step__num">3</span>We will show you the easiest way to track your expenses so that the only thing you will have to do to have rock solid books is to take a picture of the receipt and throw it away. It doesn’t get any better than that.</article>
    <article class="step step--gold"><span class="step__num">4</span>Next, we show you the importance of tax planning and why it is critical to meet with your CPA before the end of the year and not just when you do your tax preparation.</article>
    <article class="step step--white"><span class="step__num">5</span>We will show you how to hire your children and get $7,500 per child tax free. This will save you $3,000 per child in income tax reduction.</article>
    <article class="step step--gold"><span class="step__num">6</span>We will discuss how to make your child’s college education tax deductible. With college cost spiraling out of control this is a biggie.&nbsp;&nbsp; Most of our clients have a savings of about $12,000 per year of college.</article>
  </section>

  <div class="finale">
    <span class="finale__num">7</span>
    <p>Our grand finale is to show you how to use, not one, but two corporations to get a several hundred thousand dollar tax deferral, get an interest free loan from the government and use that money to grow your business and your wealth.</p>
  </div>

  <div class="rule"></div>

  <p class="slogan">If they drive by with a machine gun you don’t have to stand up.</p>

  <address class="contact">
    <div class="contact__name">Steady Ledger</div>
    <div>A Professional Accounting Corporation</div>
    <div>820 N. Orchard Ave, Ste. B, Lindale, CA 95400</div>
    <div>Phone: 555-014-2270 &nbsp;•&nbsp; Fax: 555-014-2271</div>
    <div class="contact__gap"></div>
    <div>owen@steadyledgercpas.com</div>
    <div>clara@steadyledgercpas.com</div>
    <div class="contact__web">www.steadyledgercpa.com</div>
  </address>
</main>
</body>
</html>
```